Kalm to Bloom: Prespective and Balence in People's Lives Needs a Buissness Card Design

Calm to Bloom Community Center is an organization that seeks to bring balance into people's lives. Main services include: guided meditation, group brainstorming, and guided counseling. Calm to Bloom combines Eastern practices, i.e. Buddhism, Hinduism, and Taoism, with Western practices: therapy, group brainstorming and healing. We would like a double sided card: 1) front vertical with image, 2) back horizontal with information. The main colors for the card are red, white, black. Different finishes would be nice--please no high gloss. Matte, pearlized, embossing--used tactfully and sparingly would be nice. The card should convey balance/harmony in a modern world.

```html
<!DOCTYPE html>
<html lang="en">
<head>
<meta charset="utf-8">
<title>Calm to Bloom – Business Card</title>
<link rel="stylesheet" href="https://fonts.googleapis.com/css2?family=Open+Sans:wght@300;400;600;700&family=Tinos&display=swap">
<style>
  :root {
    --page: #2a2a2a;
    --card: #1c1c1c;
    --card-ray: #262626;
    --red: #e3120b;
    --red-deep: #b80d08;
    --white: #ffffff;
    --muted: #d6d6d6;
  }
  * { margin: 0; padding: 0; box-sizing: border-box; }
  html, body { width: 1200px; height: 4018px; overflow: hidden; }
  body { background: var(--page); position: relative; font-family: "Open Sans", sans-serif; }

  .card {
    position: absolute; left: 100px; width: 1000px; height: 571px;
    background: radial-gradient(circle at 55% 50%, var(--card-ray) 0%, var(--card) 70%);
    overflow: hidden;
    box-shadow: 0 20px 50px rgba(0,0,0,.45);
  }
  .card--front { top: 900px; }
  .card--back { top: 2550px; }

  .divider { position: absolute; top: 0; bottom: 0; width: 2px; background: var(--red); }
  .card--front .divider { left: 150px; }
  .card--back .divider { left: 370px; }

  .emblem {
    position: absolute; border-radius: 50%;
    background: radial-gradient(circle at 50% 60%, var(--red) 0%, var(--red) 55%, var(--red-deep) 100%);
  }
  .card--front .emblem { width: 380px; height: 380px; left: 380px; top: 95px; }
  .card--back .emblem { width: 480px; height: 480px; left: -120px; top: 190px; }

  .wordmark {
    position: absolute; left: 172px; top: 540px;
    transform: rotate(-90deg); transform-origin: 0 0;
    color: var(--white); white-space: nowrap;
  }
  .wordmark__name { font-weight: 700; font-size: 44px; letter-spacing: 2px; line-height: 1.1; }
  .wordmark__tagline { font-weight: 300; font-size: 19px; letter-spacing: 3px; margin-top: 4px; }

  .person { position: absolute; right: 60px; top: 55px; text-align: right; color: var(--white); }
  .person__name { font-weight: 600; font-size: 40px; letter-spacing: 2px; }
  .person__role { font-weight: 300; font-size: 18px; letter-spacing: 4px; color: var(--muted); }

  .contacts { position: absolute; right: 60px; top: 245px; list-style: none; }
  .contacts li {
    display: flex; align-items: center; justify-content: flex-end; gap: 14px;
    height: 44px; font-family: "Tinos", serif; font-size: 20px; color: var(--white);
  }
  .contacts svg { width: 26px; height: 26px; display: block; }
</style>
</head>
<body>

  <section class="card card--front" aria-label="Card front">
    <div class="divider"></div>
    <div class="wordmark">
      <div class="wordmark__name">CALM TO BLOOM</div>
      <div class="wordmark__tagline">COMMUNITY CENTER</div>
    </div>
    <div class="emblem" role="img" aria-label="Red circle with black silhouette of a seated meditating figure"></div>
  </section>

  <section class="card card--back" aria-label="Card back">
    <div class="divider"></div>
    <div class="emblem" role="img" aria-label="Red circle with black silhouette of a meditating figure, cropped at the card edge"></div>
    <div class="person">
      <div class="person__name">YOUR NAME</div>
      <div class="person__role">MANAGER</div>
    </div>
    <ul class="contacts">
      <li>your address, city 11000
        <svg viewBox="0 0 26 26"><circle cx="13" cy="13" r="13" fill="#e3120b"/><path d="M13 6a4.5 4.5 0 0 0-4.5 4.5C8.5 14 13 20 13 20s4.5-6 4.5-9.5A4.5 4.5 0 0 0 13 6z" fill="#1c1c1c"/><circle cx="13" cy="10.5" r="1.6" fill="#e3120b"/></svg>
      </li>
      <li>0031 70 12 34 56
        <svg viewBox="0 0 26 26"><circle cx="13" cy="13" r="13" fill="#e3120b"/><path d="M9 7l2.5 0 1 3-1.6 1.2a8 8 0 0 0 3.9 3.9L16 13.5l3 1V17c0 1-1 1.5-2 1.4A10 10 0 0 1 7.6 9C7.5 8 8 7 9 7z" fill="#1c1c1c"/></svg>
      </li>
      <li>calmtobloom@mail.com
        <svg viewBox="0 0 26 26"><circle cx="13" cy="13" r="13" fill="#e3120b"/><rect x="7" y="9" width="12" height="8.5" fill="#1c1c1c"/><path d="M7 9l6 5 6-5" stroke="#e3120b" stroke-width="1.3" fill="none"/></svg>
      </li>
      <li>calmtobloom.com
        <svg viewBox="0 0 26 26"><circle cx="13" cy="13" r="13" fill="#e3120b"/><circle cx="13" cy="13" r="6" fill="none" stroke="#1c1c1c" stroke-width="1.6"/><path d="M7 13h12M13 7c-3 3.5-3 8.5 0 12M13 7c3 3.5 3 8.5 0 12" fill="none" stroke="#1c1c1c" stroke-width="1.3"/></svg>
      </li>
      <li>bloomblog.com
        <svg viewBox="0 0 26 26"><circle cx="13" cy="13" r="13" fill="#e3120b"/><rect x="8" y="8" width="10" height="10" rx="1.5" fill="none" stroke="#1c1c1c" stroke-width="1.6"/><path d="M10.5 11.5h5M10.5 14.5h5" stroke="#1c1c1c" stroke-width="1.3"/></svg>
      </li>
    </ul>
  </section>

</body>
</html>
```